We are looking for a new website design for our SEO WEB Development Company. The URL is www.brightlanterndigital.example

We want it to be a more powerful representation of what we do. We are also looking for a number of designers that we will give continuous business to every month. The persons design we choose will also get a proposal to complete 4 - 6 new designs for us every month for our clients.

Be creative as you can in your design submissions. We really want to stand out!

Just to give you an idea of what we like look at this site: http://www.corvexsiteworks.example/

```html
<!DOCTYPE html>
<html lang="en">
<head>
<meta charset="utf-8">
<title>Lantern Interactive Group – Web Site Design and Development</title>
<link href="https://fonts.googleapis.com/css2?family=Arimo:wght@400;700&display=swap" rel="stylesheet">
<style>
:root{
  --page:#ffffff;
  --blue-top:#3f9ad0;
  --blue-bottom:#1a6fa8;
  --blue-side:#4b9fcf;
  --ink-blue:#1a6fa8;
  --text-cyan:#1e9bd7;
  --orange:#f08a1c;
  --orange-line:#c86e1e;
  --bar-dark:#2f2f2f;
  --bar-mid:#4a4a4a;
  --side-gray:#5b6066;
  --pale-side:#e9f3fa;
  --footer:#333333;
  --white:#ffffff;
}
*{margin:0;padding:0;box-sizing:border-box}
html,body{width:1200px;height:900px;overflow:hidden;background:var(--page)}
body{font-family:"Arimo",Arial,sans-serif;position:relative}
.site{position:absolute;left:225px;top:142px;width:750px;height:615px;background:var(--pale-side)}
.abs{position:absolute}

/* header */
.header{left:0;top:0;width:750px;height:68px;background:linear-gradient(var(--blue-side),#2f86bd)}
.header-core{left:72px;top:0;width:604px;height:68px;background:linear-gradient(var(--blue-top),var(--blue-bottom))}
.brand{left:85px;top:14px;display:flex;align-items:center;gap:5px;color:var(--orange);font-weight:700;font-size:22px;letter-spacing:-.5px}
.brand-mark{width:12px;height:12px;background:var(--orange)}
.search{left:516px;top:24px;width:145px;height:22px;background:#5aa7d6;border-radius:2px;display:flex;align-items:center;padding-left:5px;gap:4px;font-size:8px;font-weight:700;color:var(--white)}
.search-field{width:84px;height:10px;background:var(--white);border:1px solid #1a5d8a}
.search-go{font-size:8px;padding:1px 2px;background:var(--white);color:var(--ink-blue);border:1px solid #1a5d8a}
.tabs{left:85px;top:50px;display:flex;gap:4px}
.tab{height:18px;padding:0 5px;background:var(--white);border:1px solid #a9d2ec;border-bottom:none;border-radius:3px 3px 0 0;font-size:10px;font-weight:700;color:#2a8fcf;line-height:18px}

/* call bar */
.callbar{left:0;top:76px;width:750px;height:44px;background:var(--side-gray);border-top:4px solid var(--orange-line);border-bottom:4px solid var(--orange-line)}
.callbar-core{left:72px;top:80px;width:604px;height:36px;background:linear-gradient(var(--bar-mid),var(--bar-dark))}
.bar-link{top:92px;display:flex;align-items:center;gap:6px;color:var(--white);font-weight:700;font-size:10px}
.phone{left:520px;top:86px;display:flex;align-items:center;gap:8px;color:var(--white);font-weight:700;font-size:17px}

/* content */
.content{left:72px;top:124px;width:604px;height:359px;background:var(--white)}
.headline{left:93px;top:135px;font-size:14px;font-weight:700;color:var(--ink-blue)}
.copy{left:93px;top:161px;width:315px;font-size:7.6px;line-height:10.3px;color:var(--text-cyan)}
.copy p{margin-bottom:10px}
.copy h3{font-size:8.5px;color:var(--ink-blue);margin:18px 0 11px}
.offer{left:467px;top:135px;font-size:12px;font-weight:700;color:var(--orange)}
.offer strong{font-size:17px}
.quote{left:465px;top:163px;width:193px;height:124px;background:linear-gradient(#2b87c3,#1b6aa2);border:1px solid #15588a;padding:6px;color:var(--white)}
.quote h2{font-size:10px;line-height:13px;font-weight:700}
.quote .hint{font-size:6px;margin-top:2px}
.field{display:flex;align-items:center;justify-content:flex-end;gap:16px;font-size:6.5px;font-weight:700;margin-top:3px;padding-right:32px}
.field span{width:80px;height:10px;background:var(--white);border:1px solid #15588a}
.quote-btn{position:absolute;left:61px;top:93px;width:67px;height:16px;background:var(--orange);border:1px solid #b05e10;color:var(--white);font-size:8px;font-weight:700;text-align:center;line-height:14px}
.portfolio{left:465px;top:305px;width:193px;height:133px;background:var(--footer);border:1px solid #222;padding:4px 6px;color:var(--white)}
.portfolio h4{font-size:8px}
.thumbs{display:grid;grid-template-columns:repeat(3,53px);gap:8px 9px;margin:5px 0 0 2px}
.thumb{height:47px}
.portfolio .hint{font-size:6px;text-align:center;margin-top:3px}
.social{left:79px;top:461px;display:flex;gap:3px}
.social span{width:17px;height:17px;border-radius:2px}

/* footer */
.footer{left:0;top:483px;width:750px;height:132px;background:var(--side-gray);border-top:3px solid #1a6fa8}
.footer-core{left:72px;top:486px;width:604px;height:129px;background:var(--footer)}
.fcol{top:497px;color:var(--white)}
.fcol h5{font-size:9px;font-weight:700;margin-bottom:2px}
.fcol li{list-style:none;font-size:7.5px;line-height:12px;padding-left:8px;position:relative}
.fcol li::before{content:"";position:absolute;left:0;top:3px;border-left:4px solid var(--orange);border-top:2.5px solid transparent;border-bottom:2.5px solid transparent}
.legal{left:72px;top:597px;width:604px;text-align:center;font-size:6.5px;font-weight:700;color:var(--white)}
</style>
</head>
<body>
<div class="site">
  <div class="abs header"></div>
  <div class="abs header-core"></div>
  <div class="abs brand"><span class="brand-mark"></span>Lantern Interactive</div>
  <div class="abs search">Search: <span class="search-field"></span><span class="search-go">Go</span></div>
  <nav class="abs tabs">
    <span class="tab">Creative Design</span><span class="tab">Website Design</span><span class="tab">Internet Marketing</span><span class="tab">IT Consultancy</span><span class="tab">Lantern</span>
  </nav>

  <div class="abs callbar"></div>
  <div class="abs callbar-core"></div>
  <div class="abs bar-link" style="left:90px">Chat to us live
    <svg width="13" height="11" viewBox="0 0 13 11"><path d="M1 1h11v7H5l-3 2V8H1z" fill="#ddd"/><path d="M3 3.5h7M3 5.5h5" stroke="#444" stroke-width="1"/></svg></div>
  <div class="abs bar-link" style="left:206px">Arrange a consultation
    <svg width="13" height="11" viewBox="0 0 13 11"><rect x="1" y="1" width="11" height="9" fill="#ddd"/><path d="M1 4h11M4 4v6M7 4v6M10 4v6M1 7h11" stroke="#555" stroke-width=".7"/></svg></div>
  <div class="abs phone">
    <svg width="20" height="14" viewBox="0 0 20 14"><path d="M1 5c0-3 18-3 18 0v2h-5V5H6v2H1z" fill="#fff"/><rect x="5" y="8" width="10" height="5" fill="#fff"/></svg>214-555-0147</div>

  <div class="abs content"></div>
  <h1 class="abs headline">Web Site Design and Development</h1>
  <div class="abs copy">
    <p>The reality these days is that your business requires a website. You must be visible on the Internet in order to assert your professionalism. What will set your business' website apart from the hundreds of others in your industry?</p>
    <p>Lantern Interactive Group is an experienced and well established web design company specializing in website design and e-commerce development. With our team's combined experience in graphic design, web application development, Flash animation and e-commerce programming, you can be confident that whatever your project demands, our web developers can deliver on time and on budget!</p>
    <p>Our web designers have the creative talent to appeal to your sense of style, the training and knowledge of current web development standards and practices, and the ability to turn your ideas into reality!</p>
    <p>We design sites for clients ranging from small start-up companies needing a basic web presence to large corporations requiring complex web applications.</p>
    <p>Please complete our form to request a no cost, no obligation quote today!</p>
    <h3>Don't believe the hype!</h3>
    <p>Don't just take our word for it that we design quality websites and Multi Media projects that promote your company, perform conversions and generate sales leads. See our portfolio for examples of web design and internet marketing that we have done for clients in and outside of Dallas, Texas.</p>
  </div>

  <div class="abs offer">Special offer starts at <strong>$199.00</strong></div>
  <form class="abs quote">
    <h2>Let us give you a FREE, no obligation quote to provide you a new website</h2>
    <div class="hint">Fill in the fields below:</div>
    <div class="field">Name: <span></span></div>
    <div class="field">Email: <span></span></div>
    <div class="field">Telephone: <span></span></div>
    <div class="quote-btn">Get quote &gt;&gt;</div>
  </form>

  <section class="abs portfolio">
    <h4>Portfolio</h4>
    <div class="thumbs">
      <div class="thumb" role="img" aria-label="Client website screenshot, green and cream layout" style="background:linear-gradient(#6f8f4a,#d9d2b4)"></div>
      <div class="thumb" role="img" aria-label="Client website screenshot, blue layout" style="background:linear-gradient(#2c6fa8,#9cc3de)"></div>
      <div class="thumb" role="img" aria-label="Client website screenshot, white and purple layout" style="background:linear-gradient(#e8e8f0,#8a7bb0)"></div>
      <div class="thumb" role="img" aria-label="Client website screenshot, blue and white layout" style="background:linear-gradient(#3d84c0,#e3edf5)"></div>
      <div class="thumb" role="img" aria-label="Client website screenshot, black and gold layout" style="background:linear-gradient(#111,#3a3412)"></div>
      <div class="thumb" role="img" aria-label="Client website screenshot, tan and brown layout" style="background:linear-gradient(#b59a62,#6b4a2c)"></div>
    </div>
    <div class="hint">Click on a thumbnail to see the full site</div>
  </section>

  <div class="abs social">
    <span style="background:#3b5a98"></span><span style="background:#3fa9d8"></span><span style="background:#1b6f9f"></span><span style="background:#f08a1c"></span>
  </div>

  <footer>
    <div class="abs footer"></div>
    <div class="abs footer-core"></div>
    <div class="abs fcol" style="left:105px"><h5>Creative Design</h5><ul><li>Creative Advertising</li><li>Print Design</li><li>Corporate Identity</li><li>Packaging</li></ul></div>
    <div class="abs fcol" style="left:225px"><h5>Internet Marketing Services</h5><ul><li>Search Engine Optimization</li><li>Pay-per-Click Campaign Consulting</li><li>Email Marketing</li><li>SEO Copywriting</li><li>Reputation Management</li></ul></div>
    <div class="abs fcol" style="left:390px"><h5>Website Design</h5><ul><li>Web Design</li><li>E-commerce</li><li>Multimedia</li><li>Web Application Development</li></ul></div>
    <div class="abs fcol" style="left:535px"><h5>IT Consulting</h5><h5 style="margin-top:10px">Lantern Interactive</h5><ul><li>About Us</li><li>Our Work</li><li>Contact Us</li></ul></div>
    <div class="abs legal">© 2011 Lantern Interactive Group - 4820 North Harwood Parkway Dallas, TX 75201-0000</div>
  </footer>
</div>
</body>
</html>
```